Brume vodka

With the logo attached in the subsequent file, a business card that reflects a premium and organic vodka. On the first side, the company logo in large. The names must be included on the back of the card (Miguel Ángel Tomás Ferrandis with the number +34 655 271 389 and Pau Berenguer Casals and +34 677 314 920). The slogan "What binds us" and "Organic and permium vodka" in bold E-mail (brumevodka@mailfield.net); Website www.brumevodkaorg.net

```html
<!DOCTYPE html>
<html lang="en">
<head>
<meta charset="utf-8">
<title>Brume Vodka – Business Card</title>
<link rel="stylesheet" href="https://fonts.googleapis.com/css2?family=Gelasio:wght@400;700&family=Open+Sans:wght@400;500&display=swap">
<style>
  :root {
    --backdrop: #e8e5e0;
    --card-white: #f3f3f2;
    --slate: #7b7d81;
    --logo-grey: #8c8d90;
    --ink-light: #ffffff;
    --serif: "Gelasio", Georgia, serif;
    --sans: "Open Sans", Arial, sans-serif;
  }
  * { margin: 0; padding: 0; box-sizing: border-box; }
  html, body {
    width: 900px;
    height: 1200px;
    overflow: hidden;
    background: var(--backdrop);
  }
  .card {
    position: absolute;
    border-radius: 18px;
    overflow: hidden;
  }
  /* Front */
  .card-front {
    left: 78px; top: 137px;
    width: 762px; height: 433px;
    background: var(--card-white);
  }
  .brand {
    position: absolute;
    left: 0; right: 0; top: 190px;
    text-align: center;
    font-family: var(--serif);
    font-weight: 400;
    color: var(--logo-grey);
  }
  .brand-name {
    display: block;
    font-size: 132px;
    line-height: 1;
    letter-spacing: 2px;
    text-transform: uppercase;
  }
  .brand-sub {
    display: block;
    margin-top: 14px;
    font-size: 27px;
    letter-spacing: 5px;
    text-transform: uppercase;
  }
  /* Back */
  .card-back {
    left: 77px; top: 630px;
    width: 766px; height: 436px;
    background: var(--slate);
  }
  .card-back svg { position: absolute; inset: 0; }
  .contact {
    position: absolute;
    left: 0; right: 0;
    text-align: center;
    color: var(--ink-light);
  }
  .contact-name {
    font-family: var(--serif);
    font-weight: 700;
    font-size: 27px;
    line-height: 1;
  }
  .contact-phone {
    font-family: var(--sans);
    font-size: 21px;
    letter-spacing: 1px;
    line-height: 1;
    margin-top: 8px;
  }
  .contact-one { top: 36px; }
  .contact-two { top: 114px; }
  .tagline {
    position: absolute;
    left: 0; right: 0; top: 287px;
    text-align: center;
    color: var(--ink-light);
  }
  .tagline-title {
    display: flex;
    justify-content: center;
    align-items: center;
    gap: 14px;
    font-family: var(--serif);
    font-size: 27px;
    line-height: 1;
  }
  .tagline-title::before,
  .tagline-title::after {
    content: "";
    width: 72px;
    height: 2px;
    background: var(--ink-light);
  }
  .tagline-sub {
    font-family: var(--serif);
    font-weight: 700;
    font-size: 20px;
    margin-top: 8px;
    line-height: 1;
  }
  .web-line {
    position: absolute;
    left: 0; right: 0; top: 382px;
    text-align: center;
    font-family: var(--sans);
    font-size: 21px;
    color: var(--ink-light);
    line-height: 1;
  }
</style>
</head>
<body>
  <section class="card card-front" aria-label="Card front">
    <h1 class="brand">
      <span class="brand-name">Brume</span>
      <span class="brand-sub">vodka</span>
    </h1>
  </section>

  <section class="card card-back" aria-label="Card back">
    <svg width="766" height="436" viewBox="0 0 766 436" aria-hidden="true">
      <path fill="var(--card-white)"
        d="M0,55 C110,62 140,190 230,200 L540,200 C630,190 660,70 766,52
           L766,392 C660,390 640,250 560,236 L210,236 C120,250 110,382 0,388 Z"/>
    </svg>

    <div class="contact contact-one">
      <p class="contact-name">Miguel Ángel Tomás Ferrandis</p>
      <p class="contact-phone">+34 655 271 389</p>
    </div>
    <div class="contact contact-two">
      <p class="contact-name">Pau Berenguer Casals</p>
      <p class="contact-phone">+34 677 314 920</p>
    </div>

    <div class="tagline">
      <p class="tagline-title">What Binds Us</p>
      <p class="tagline-sub">Organic And Permium Vodka</p>
    </div>

    <p class="web-line">brumevodka@mailfield.net | www.brumevodkaorg.net</p>
  </section>
</body>
</html>
```